Stationery Design Project

We need a stationery design for our Norwegian trucking company. We have existed for about 15 years and our 12 drivers uses relatively new vehicles to transport goods around in northern Norway. Long distance routes with fresh fish og food transport is our main operations.

We have already made alogo that's printed on our trucks. The logo and a picture of our trucks is attached. I think the logo i crappy, but since its already in use, changing it is not an option in this round. Still using a better colour scheme in the overall stationery and more interesting fonts is possible (altso in the logo).

Company details:
Name: Vikstrandbil AS
Organisation nr 981 537 608
Post adress: 8613 Lysvær

I like minimalism and simplicity. I am avalibly for questions in normal GMT working hours either here or on mail: petter@vikstrand.no

Reason: Hi. Im extending the deadline because I needed some time to find a vector file of our logo. Sorry for the inconvenience

Hi, and thanks for all your interest in the project. Some updates:

-          I have decided to commit to using one of the designs. Some designer will get the payment.

-          I have extended the deadline with 24 hours since I needed some time to find our firms vector logo (a slow Swedish man was holding me up)

-          We will not choose a design before the deadline. No need to rush.

-          We have received a lot of great design and think there is a need to specified the product we want to make:

o   Business Card for all our employers. I just need the design and will duplicate with the correct numbers and name myself. The information on should be: Logo, employer’s name, Phone number, email, website, Postal number and address. Use this as a template: logo, Leif Brattli, 47283916, Leif@vikstrand.no,, vikstrand.no, 8613 Lysvær. The order and placement of the information is your creative decision.

o   Stickers to put on the goods we travel. On the sticker the should be the following information: Logo, phone number, Tekst and link: Fraktæ av Vikstrandbil. Ke du syns? Vikstrand.no/tilbakemelding (this means: Handled by Vikstrandbil. What do you think Vikstrand.no/feedback -à the link will be a feedback form). The placement the information and size is your creative decision with some stings: we have been thinking of using Prentavo for printing and see that a size about 6x6 cm, 8x5 or something like that. (with 3000 copies our budget is 200 punds). Any suggestions of other suppliers are welcome. Prentavo price calculator http://www.prentavoprint.co.uk/digital-litho-printing/printing-labels-tags/stickers/

o   Letterhead with logo, address, phone number and organizational number.

o   Envelopes with logo,address, phone number and organizational number.

Have a nice day.

 

 

• Using the blue colour in the logo and using a similar graphic approch.

```html
<!DOCTYPE html>
<html lang="no">
<head>
<meta charset="utf-8">
<title>Vikstrandbil – visittkort</title>
<link rel="stylesheet" href="https://fonts.googleapis.com/css2?family=Open+Sans:wght@400;600;700&display=swap">
<style>
  :root {
    --backdrop: #c9ccd0;
    --card-white: #ffffff;
    --brand-navy: #0b4d9e;
    --brand-blue: #0a76bf;
    --text-dark: #2b2b2b;
    --card-edge: #8a8d91;
  }
  * { box-sizing: border-box; margin: 0; padding: 0; }
  html, body { width: 1200px; height: 751px; overflow: hidden; }
  body {
    position: relative;
    background: var(--backdrop);
    font-family: "Open Sans", sans-serif;
  }
  .card {
    position: absolute;
    width: 525px;
    height: 299px;
    border-radius: 22px;
    overflow: hidden;
  }
  .card--front { left: 50px; top: 50px; background: var(--card-white); border: 1px solid var(--card-edge); }
  .card--back-white { left: 620px; top: 50px; background: var(--card-white); border: 1px solid var(--card-edge); }
  .card--back-navy { left: 50px; top: 388px; background: var(--brand-navy); }
  .card--back-blue { left: 620px; top: 388px; background: var(--brand-blue); }

  .brand {
    position: absolute;
    left: 0; right: 0;
    display: flex;
    align-items: center;
    justify-content: center;
    gap: 14px;
    font-weight: 700;
    font-size: 46px;
    letter-spacing: -0.5px;
    color: var(--brand-navy);
  }
  .brand__dot {
    width: 22px; height: 22px;
    border-radius: 50%;
    background: currentColor;
  }
  .card--front .brand { top: 62px; }
  .card--back-white .brand,
  .card--back-navy .brand,
  .card--back-blue .brand { top: 120px; }
  .card--back-navy .brand,
  .card--back-blue .brand { color: var(--card-white); }

  .web {
    position: absolute;
    left: 0; right: 0;
    top: 248px;
    text-align: center;
    font-size: 17px;
    letter-spacing: 3.4px;
    color: var(--text-dark);
  }
  .card--back-navy .web,
  .card--back-blue .web { color: var(--card-white); }

  .contact {
    position: absolute;
    top: 167px;
    font-size: 15px;
    line-height: 22px;
    color: var(--text-dark);
  }
  .contact--person { right: 282px; text-align: right; }
  .contact--company { left: 268px; }
  .contact__name { font-weight: 700; font-size: 18px; color: var(--brand-navy); }
  .contact__label { color: var(--brand-navy); }
  .contact__row { display: flex; align-items: center; gap: 5px; white-space: nowrap; }
  .contact--person .contact__row { justify-content: flex-end; }
  .contact__icon { width: 11px; height: 11px; fill: var(--brand-navy); flex: none; }
  .contact__divider {
    position: absolute;
    left: 256px; top: 168px;
    width: 1px; height: 66px;
    background: #9aa6b5;
  }
  .front-band {
    position: absolute;
    left: 0; right: 0; bottom: 0;
    height: 52px;
    background: linear-gradient(90deg, var(--brand-navy), var(--brand-blue));
  }
</style>
</head>
<body>

  <section class="card card--front">
    <div class="front-band" role="img" aria-label="Decorative blue wave band along the bottom edge"></div>

    <div class="brand"><span class="brand__dot"></span>Vikstrandbil</div>

    <div class="contact contact--person">
      <div class="contact__name">Leif Brattli</div>
      <div class="contact__row">
        <svg class="contact__icon" viewBox="0 0 12 12"><path d="M1 6 L6 2 L11 6 V11 H1 Z"/></svg>8613 Lysvær
      </div>
      <div class="contact__row">
        <svg class="contact__icon" viewBox="0 0 12 12"><path d="M2 1 L5 1 L6 4 L4.5 5.2 C5.2 6.8 5.8 7.4 7 7.8 L8 6 L11 7 L11 10 C6 11 1 6 2 1 Z"/></svg>47283916
      </div>
    </div>

    <div class="contact__divider"></div>

    <div class="contact contact--company">
      <div class="contact__row"><span class="contact__label">Org nr</span> 981 537 608</div>
      <div class="contact__row">
        <svg class="contact__icon" viewBox="0 0 12 12"><path d="M1 3 H11 V10 H1 Z M1 3 L6 7 L11 3" stroke="#fff" stroke-width="0.8"/></svg>Leif@vikstrand.no
      </div>
      <div class="contact__row">
        <svg class="contact__icon" viewBox="0 0 12 12"><circle cx="6" cy="6" r="5"/><path d="M1 6 H11 M6 1 V11" stroke="#fff" stroke-width="0.8"/></svg>www.vikstrand.no
      </div>
    </div>
  </section>

  <section class="card card--back-white">
    <div class="brand"><span class="brand__dot"></span>Vikstrandbil</div>
    <div class="web">www.vikstrand.no</div>
  </section>

  <section class="card card--back-navy">
    <div class="brand"><span class="brand__dot"></span>Vikstrandbil</div>
    <div class="web">www.vikstrand.no</div>
  </section>

  <section class="card card--back-blue">
    <div class="brand"><span class="brand__dot"></span>Vikstrandbil</div>
    <div class="web">www.vikstrand.no</div>
  </section>

</body>
</html>
```